Luxury International Regenerative Medicine Center

Need marketing brochure to raise money for Luxury Regenerative Medicine in Dubai. This is fashioned after www.Velorin.net and is membership only and very expensive and all about Stem Cell treatment and Wellness

```html
<!DOCTYPE html>
<html lang="en">
<head>
<meta charset="utf-8">
<title>Lumora Clinic Brochure</title>
<link href="https://fonts.googleapis.com/css2?family=Mulish:ital,wght@0,400;0,600;1,400;1,700&family=Questrial&display=swap" rel="stylesheet">
<style>
:root{
  --ink:#1d1d1d;
  --grey:#5a5a5a;
  --soft:#cfcfcf;
  --orange:#ef5a1f;
  --logo-grey:#555;
  --paper:#ffffff;
  --frame:#3a3a3a;
}
*{margin:0;padding:0;box-sizing:border-box}
html,body{width:1200px;height:907px;overflow:hidden;background:var(--paper)}
body{font-family:"Mulish",sans-serif;color:var(--ink);position:relative}
.spread{position:absolute;inset:0;border:1px solid var(--frame)}
.page{position:absolute;top:0;height:907px;width:600px;overflow:hidden}
.page--left{left:0}
.page--right{left:600px;background:linear-gradient(90deg,#e4e4e4 0,#fff 40px)}
.page--left::after{content:"";position:absolute;right:0;top:0;width:30px;height:100%;background:linear-gradient(90deg,#fff,#ececec)}
.page-corner{position:absolute;right:0;bottom:0;width:60px;height:60px;background:var(--orange);clip-path:polygon(100% 0,100% 100%,0 100%)}
.page-number{position:absolute;right:14px;bottom:8px;color:#fff;font-family:"Questrial",sans-serif;font-size:17px}
.brand{position:absolute;left:185px;top:26px;display:flex;align-items:center;gap:10px}
.brand-mark{width:30px;height:30px;border-radius:50%;background:var(--orange)}
.brand-name{font-family:"Questrial",sans-serif;font-size:27px;color:var(--logo-grey);line-height:1}
.welcome-rule{position:absolute;left:115px;top:90px;width:332px;border-top:1px solid var(--grey)}
.welcome{position:absolute;left:115px;top:96px;width:332px;text-align:center;font-family:"Questrial",sans-serif;font-size:12.5px}
.photo-circle{position:absolute;border-radius:50%}
.dots{position:absolute;left:263px;top:262px;display:grid;grid-template-columns:12px 12px;gap:5px}
.dots span{width:12px;height:12px;border-radius:50%;background:#555}
.dots span.accent{background:var(--orange)}
.intro{position:absolute;left:118px;top:450px;width:322px;font-size:12.6px;line-height:15.6px;color:#333}
.intro p{text-align:justify;margin-bottom:17px;position:relative}
.intro p.bullet::before{content:"";position:absolute;left:-14px;top:3px;border-left:7px solid #888;border-top:4.5px solid transparent;border-bottom:4.5px solid transparent}
.intro p.closing{font-style:italic;text-align:left}
.side-rule{position:absolute;left:439px;top:453px;height:425px;border-left:1px solid #bbb}
.side-rule-tip{position:absolute;left:433px;top:874px;width:13px;height:13px;border-radius:50%;background:#bbb}
.side-flag{position:absolute;left:440px;top:453px;border-top:7px solid #bbb;border-right:10px solid transparent}
.side-word{position:absolute;left:446px;top:470px;writing-mode:vertical-rl;font-family:"Questrial",sans-serif;font-size:40px;color:#e6e6e6;letter-spacing:2px}
.ribbon{position:absolute;border-radius:40px;background:linear-gradient(180deg,rgba(200,200,200,0) 0,rgba(200,200,200,.45) 50%,rgba(200,200,200,0) 100%)}
.hero{position:absolute;left:140px;top:0;width:320px;height:300px;background:radial-gradient(ellipse at 50% 40%,#f1d6c6 0,#e8c3ad 45%,#fff 72%)}
.section-rule{position:absolute;left:20px;width:560px;border-top:1px solid #444}
.section-divider{position:absolute;left:133px;border-left:1px solid #444}
.section-title{position:absolute;right:475px;width:130px;text-align:right;font-style:italic;font-weight:700;font-size:18px;line-height:25px}
.section-body{position:absolute;left:144px;width:298px;font-style:italic;font-size:12.6px;line-height:15px;color:#333}
.thumb{position:absolute;left:446px;width:96px;height:62px}
</style>
</head>
<body>
<div class="spread">
  <section class="page page--left">
    <div class="brand"><span class="brand-mark"></span><span class="brand-name">Lumora Clinic</span></div>
    <div class="welcome-rule"></div>
    <p class="welcome">Welcome to Lumora Clinic and Cell Theraphy Facility</p>

    <div class="photo-circle" style="left:128px;top:122px;width:150px;height:150px;background:radial-gradient(circle at 40% 40%,#e8f0f8,#5b84b8 80%)" role="img" aria-label="Doctor touching a digital medical interface"></div>
    <div class="photo-circle" style="left:288px;top:122px;width:150px;height:150px;background:radial-gradient(circle at 50% 40%,#f0e4dc,#8a6a5a 85%)" role="img" aria-label="Scientists examining a sample in the laboratory"></div>
    <div class="dots"><span></span><span class="accent"></span><span></span><span></span></div>
    <div class="photo-circle" style="left:132px;top:287px;width:145px;height:148px;background:radial-gradient(circle at 55% 40%,#e9eef2,#7c8894 85%)" role="img" aria-label="Researcher looking through a microscope"></div>
    <div class="photo-circle" style="left:292px;top:290px;width:144px;height:144px;background:radial-gradient(circle at 50% 40%,#f3ece6,#7a8aa8 85%)" role="img" aria-label="Laboratory team inspecting a test tube"></div>

    <div class="ribbon" role="img" aria-label="Faint helix decoration" style="left:450px;top:650px;width:110px;height:240px"></div>
    <div class="side-rule"></div><div class="side-flag"></div><div class="side-rule-tip"></div>
    <div class="side-word">Lumora</div>

    <div class="intro">
      <p class="bullet">The Lumora Clinic PC is among the first clinical practices to offer Regenerative Medicine treatments to its patients as well as traditional surgical practices in orthopedics, aesthetic medicine, urology, and more.</p>
      <p class="bullet">Regenerative Medicine is an exciting new area in the treatment of many conditions that have been very difficult for your physician to treat. The Lumora medical staff is concentrated on using what we call "autologous", your own cells, in our treatments.</p>
      <p class="bullet">The cells are returned to your physician in about 1 hour where he or she can begin your treatment. To date, patients have received treatment for osteoarthritis, rheumatoid arthritis, multiple sclerosis, medical aesthetics for fine lines and wrinkles, sports medicine injuries, and more.</p>
      <p class="bullet">The Lumora physicians practice from a state of the art surgical facility that was built in 2012 in Manhattan, New York. The facility features a number of special treatment rooms and surgical suites for orthopedic and other surgical procedures.</p>
      <p class="closing">We strive to make the experience for you, our patient, as professional and personalized as possible.</p>
    </div>
    <div class="page-corner"></div><span class="page-number">1</span>
  </section>

  <section class="page page--right">
    <div class="hero" role="img" aria-label="Woman with closed eyes holding her face, smooth skin portrait"></div>
    <div class="ribbon" role="img" aria-label="Faint helix decoration" style="left:390px;top:320px;width:150px;height:560px"></div>

    <div class="section-rule" style="top:301px"></div>
    <div class="section-divider" style="top:302px;height:106px"></div>
    <h2 class="section-title" style="top:330px">Surgical Specialties</h2>
    <p class="section-body" style="top:315px">Lumora Clinic PC offers our patients multiple surgical specialties. We have cosmetic dermatologists, plastic surgeons, sports medicine orthopedics and urologist on staff. We can take care of almost all surgical needs with the finest most deadicated physicians.</p>
    <div class="thumb" style="top:320px;background:linear-gradient(135deg,#c0303a,#e9d8d0 55%,#8a7466)" role="img" aria-label="Researchers with cell culture plates"></div>

    <div class="section-rule" style="top:448px"></div>
    <div class="section-divider" style="top:449px;height:90px"></div>
    <h2 class="section-title" style="top:468px">Cellular Therapies</h2>
    <p class="section-body" style="top:461px">The one major advantage of Lumora Clinic is we offer cellular therapy for patients that have failed with conventional surgery or medical treatments. We address unmet clinical needs and offer the most advanced cellular therapy in the world</p>
    <div class="thumb" style="top:460px;background:linear-gradient(135deg,#3a7fa8,#dfeaf0 55%,#2e8f88)" role="img" aria-label="Scientist in mask handling a petri dish"></div>

    <div class="section-rule" style="top:575px"></div>
    <div class="section-divider" style="top:576px;height:110px"></div>
    <h2 class="section-title" style="top:590px">Our<br>Staff</h2>
    <p class="section-body" style="top:587px">Our staff is composed of the finest and most caring professionals in the world. In addition to skilled medical care we offer the ultimate in service. We provide individual personalized medicine at its best. We will devote the time and energy needed to make you better and meet your every need</p>
    <div class="thumb" style="top:590px;background:linear-gradient(135deg,#e9ecee,#8d9aa5 60%,#50606c)" role="img" aria-label="Laboratory staff working at benches"></div>

    <div class="section-rule" style="top:708px"></div>
    <div class="section-divider" style="top:709px;height:98px"></div>
    <h2 class="section-title" style="top:720px">Physicians Portal</h2>
    <p class="section-body" style="top:720px">The physicians at Lumora Clinic are pioneering a new and exciting group of treatments in Regenerative Medicine. For the past several years, researchers have identified and have been working with a group of cells referred to as stromal vascular fraction or SVF.</p>
    <div class="thumb" style="top:722px;background:linear-gradient(135deg,#6a4a3a,#e8d2c2 50%,#caa56a)" role="img" aria-label="Two physicians reviewing records together"></div>

    <div class="page-corner"></div><span class="page-number">2</span>
  </section>
</div>
</body>
</html>
```